Browvella Rack Card

I would like to have my price list on part of the flyer if you can look on our website
WWW.BROWVELLAPK.EXAMPLE
Eye Lash Extension Studio and Spa.

Facials
Waxing
Make Up
Bridal Packages
KORI Lash Lift

```html
<!DOCTYPE html>
<html lang="en">
<head>
<meta charset="utf-8">
<title>Browvella Rack Card</title>
<link rel="stylesheet" href="https://fonts.googleapis.com/css2?family=Questrial&display=swap">
<style>
  :root {
    --page: #e4e2e0;
    --dark: #3b3b3d;
    --dark-glow: #5a5a5c;
    --purple: #8d3c8e;
    --purple-light: #a24fa2;
    --pink: #d792cd;
    --marble: #ececec;
    --white: #ffffff;
    --ink: #2a2a2a;
  }
  * { box-sizing: border-box; margin: 0; padding: 0; }
  html, body { width: 1200px; height: 1010px; overflow: hidden; background: var(--page); }
  body { font-family: "Questrial", "Century Gothic", sans-serif; position: relative; }

  .card {
    position: absolute; top: 42px; width: 426px; height: 925px;
    overflow: hidden; box-shadow: 0 6px 18px rgba(0,0,0,.25); background: var(--dark);
  }
  .card--front { left: 130px; }
  .card--back { left: 644px; }
  .card-bg { position: absolute; inset: 0; }
  .abs { position: absolute; }

  .brand-name { font-size: 24px; color: var(--ink); letter-spacing: .5px; }
  .brand-tag { font-size: 11px; color: var(--ink); letter-spacing: .5px; }
  .label-mark { font-size: 20px; letter-spacing: 4px; color: var(--white); }

  .headline { color: var(--pink); font-size: 25px; line-height: 31px; }
  .body-copy { color: var(--white); font-size: 13px; line-height: 17px; text-align: justify; }

  .service-list { list-style: none; color: var(--white); }
  .service-list li { position: relative; padding-left: 17px; }
  .service-list li::before {
    content: ""; position: absolute; left: 0; top: 50%; width: 11px; height: 11px;
    margin-top: -6px; border-radius: 50%; background: var(--white);
  }
  .service-list li::after {
    content: ""; position: absolute; left: 3px; top: 50%; width: 3px; height: 3px;
    margin-top: -3px; border-right: 1.5px solid var(--dark); border-top: 1.5px solid var(--dark);
    transform: rotate(45deg);
  }
  .service-list--front { font-size: 17px; line-height: 23px; }
  .service-list--back { font-size: 17px; line-height: 23px; }

  .partner-box {
    background: #111; color: var(--white); font-size: 13px; letter-spacing: 1px;
    display: flex; align-items: center; justify-content: center;
  }
  .web { color: var(--ink); font-size: 17px; }
  .web--back { color: var(--pink); font-size: 24px; }

  .cta-band {
    background: var(--purple); color: var(--white); font-size: 26px;
    display: flex; align-items: center; justify-content: center;
  }
  .phone { color: var(--white); font-size: 24px; font-weight: 700; display: flex; align-items: center; gap: 14px; }
  .address { color: var(--white); font-size: 16px; }
</style>
</head>
<body>

<!-- Front card -->
<section class="card card--front">
  <svg class="card-bg" width="426" height="925" viewBox="0 0 426 925">
    <defs>
      <linearGradient id="heroTone" x1="0" y1="0" x2="1" y2="1">
        <stop offset="0" stop-color="#e8d2b4"/>
        <stop offset=".5" stop-color="#d6a98a"/>
        <stop offset="1" stop-color="#b58f6a"/>
      </linearGradient>
      <radialGradient id="darkGlow" cx=".5" cy=".35" r=".7">
        <stop offset="0" stop-color="var(--dark-glow)"/>
        <stop offset="1" stop-color="var(--dark)"/>
      </radialGradient>
      <linearGradient id="lashTone" x1="0" y1="0" x2="1" y2="1">
        <stop offset="0" stop-color="#e9ddd6"/>
        <stop offset="1" stop-color="#8c7468"/>
      </linearGradient>
      <linearGradient id="boxPurple" x1="0" y1="0" x2="1" y2="0">
        <stop offset="0" stop-color="var(--purple)"/>
        <stop offset="1" stop-color="var(--purple-light)"/>
      </linearGradient>
    </defs>
    <rect width="426" height="380" fill="url(#heroTone)" role="img" aria-label="Portrait photo of a blonde woman with lash extensions"/>
    <path d="M0,350 C110,305 250,300 426,345 L426,925 L0,925 Z" fill="var(--purple)"/>
    <path d="M0,362 C110,318 250,314 426,356 L426,925 L0,925 Z" fill="url(#darkGlow)"/>
    <path d="M0,672 C90,735 250,710 426,640 L426,925 L0,925 Z" fill="var(--white)"/>
    <path d="M0,690 C90,748 250,725 426,660 L426,925 L0,925 Z" fill="var(--marble)"/>
    <path d="M37,716 C140,712 250,690 385,655 L385,843 Q385,858 370,858 L52,858 Q37,858 37,843 Z" fill="url(#boxPurple)"/>
    <circle cx="352" cy="392" r="82" fill="url(#lashTone)" stroke="var(--purple)" stroke-width="5" role="img" aria-label="Close-up photo of an eye with lash extensions"/>
    <rect x="253" y="698" width="114" height="72" rx="4" fill="#c9b6ad" stroke="var(--white)" stroke-width="2" role="img" aria-label="Before photo of natural lashes"/>
    <rect x="253" y="772" width="114" height="72" rx="4" fill="#8f7d78" stroke="var(--white)" stroke-width="2" role="img" aria-label="After photo of lifted lashes"/>
    <circle cx="366" cy="893" r="24" fill="#d9d4cc"/>
    <circle cx="72" cy="300" r="40" fill="#f4efe6" stroke="var(--white)" stroke-width="2"/>
  </svg>

  <div class="abs label-mark" style="left:28px;top:48px;">LUMORA LASHES</div>

  <div class="abs" style="left:20px;top:375px;">
    <div class="brand-name" style="color:var(--white);">Browvella NJ</div>
    <div class="brand-tag" style="color:var(--white);">Lumora Lash Studio</div>
  </div>

  <h1 class="abs headline" style="left:20px;top:440px;font-weight:400;">Eye Lash Extension<br>Studio and Spa.</h1>

  <p class="abs body-copy" style="left:22px;top:528px;width:384px;">KORI Lash Lift is a new keratin based lash enhancement treatment. Instead of doing a traditional perm that simply curves your lashes, A Lash Lift actually turns the eyelashes upwards and adds tint to give them length, height and volume, and an appearance of having longer and thicker lashes.</p>

  <ul class="abs service-list service-list--front" style="left:60px;top:726px;">
    <li>Facials</li>
    <li>Waxing</li>
    <li>Make Up</li>
    <li>Bridal Packages</li>
    <li>KORI Lash Lift</li>
  </ul>

  <div class="abs partner-box" style="left:20px;top:875px;width:96px;height:36px;">KORI LASHES</div>
  <div class="abs web" style="left:134px;top:882px;">www.browvellapk.example</div>
</section>

<!-- Back card -->
<section class="card card--back">
  <svg class="card-bg" width="426" height="925" viewBox="0 0 426 925">
    <defs>
      <radialGradient id="darkGlowBack" cx=".5" cy=".4" r=".7">
        <stop offset="0" stop-color="var(--dark-glow)"/>
        <stop offset="1" stop-color="var(--dark)"/>
      </radialGradient>
      <linearGradient id="facialTone" x1="0" y1="0" x2="1" y2="1">
        <stop offset="0" stop-color="#a98a74"/>
        <stop offset=".5" stop-color="#e6d8cc"/>
        <stop offset="1" stop-color="#c7aa92"/>
      </linearGradient>
      <linearGradient id="portraitTone" x1="0" y1="0" x2="0" y2="1">
        <stop offset="0" stop-color="#f0e4cf"/>
        <stop offset="1" stop-color="#2a2a2a"/>
      </linearGradient>
    </defs>
    <rect width="426" height="925" fill="url(#darkGlowBack)"/>
    <path d="M0,0 L426,0 L426,158 C300,178 150,185 0,150 Z" fill="var(--purple)"/>
    <path d="M0,0 L426,0 L426,150 C300,170 150,176 0,142 Z" fill="var(--marble)"/>
    <circle cx="218" cy="58" r="46" fill="#f6f3ee" stroke="#d6d1ca" stroke-width="2"/>
    <ellipse cx="342" cy="418" rx="57" ry="72" fill="url(#portraitTone)" stroke="var(--white)" stroke-width="3" role="img" aria-label="Portrait photo of the studio stylist"/>
    <rect x="0" y="565" width="426" height="210" fill="url(#facialTone)" role="img" aria-label="Photo of a woman receiving a facial mask treatment"/>
    <path d="M0,772 C140,740 290,740 426,768 L426,925 L0,925 Z" fill="var(--purple)"/>
    <path d="M0,780 C140,750 290,750 426,776 L426,925 L0,925 Z" fill="url(#darkGlowBack)"/>
  </svg>

  <div class="abs" style="left:0;top:122px;width:426px;text-align:center;">
    <div class="brand-name">Browvella NJ</div>
    <div class="brand-tag">Lumora Lash Studio</div>
  </div>

  <h2 class="abs headline" style="left:0;top:205px;width:426px;text-align:center;font-weight:400;font-size:26px;">Facial Enhancements</h2>

  <p class="abs body-copy" style="left:19px;top:265px;width:390px;text-align:left;">Upgrade your treatments by choosing one or more of our carefully created service enhancements. Enhancements are available as incorporated additions to facial and lash services without adding additional time to the treatment</p>

  <ul class="abs service-list service-list--back" style="left:19px;top:352px;">
    <li>Facial Waxing</li>
    <li>Body Waxing</li>
    <li>Tinting</li>
    <li>Signature Facials</li>
    <li>Microdermabrasion</li>
  </ul>

  <div class="abs cta-band" style="left:0;top:494px;width:426px;height:70px;">Book Your Treatment Today</div>

  <div class="abs phone" style="left:100px;top:790px;">
    <svg width="34" height="34" viewBox="0 0 34 34" aria-hidden="true">
      <circle cx="17" cy="17" r="15" fill="none" stroke="var(--white)" stroke-width="2.5"/>
      <path d="M11.5,9.5 L14.5,9 L16,13 L14,14.6 C15,17 17,19 19.4,20 L21,18 L25,19.5 L24.5,22.5 C24.2,23.6 23,24.5 21.6,24.3 C15,23.3 10.7,19 9.7,12.4 C9.5,11 10.4,9.8 11.5,9.5 Z" fill="var(--white)"/>
    </svg>
    <span>555-013-2846</span>
  </div>

  <div class="abs address" style="left:0;top:880px;width:426px;text-align:center;top:842px;">2190 Willow Crest Road, Fairhaven, NJ 07000</div>

  <div class="abs web web--back" style="left:0;top:875px;width:426px;text-align:center;">www.browvellapk.example</div>
</section>

</body>
</html>
```